Promotion Banner on Website Homepage

Needing a four designs for our website homepage. our web address is: www.brisktailcourier.com
I like the colors used for the current banners that came stock with the website. And I like that the whole banner is not solid in color or graphic.
The four designs we need will take the place of the four images calling attention to the sale items.
Each banner final size is 228 x 228 pixels.
Specifics for each banner are as follows:
1. (Text) Made in Wisconsin (Image) State of Wisconsin outline in the back with the text over it.
2. (Text) The most awarded pet food (Image) Valmora is the brand that this will relate to. Can use the company logo or use an image of their Adult dog food from their website at: www.valmora.ca
3. (Text) Bulk Treats, get up to 25% off (image) (open to options)
4. (Text) 100% Natural. No Preservatives. No Additives. Authentic. Corvale Pup Gnaw. (image) (open to options)
Industry/Entity Type
Pet
Requirements
Must have
- Should use the same colors that are currently used on the banners that I wish to replace.
Green, orange, blue.
Should not have
- Do not include paws, graphics that do not relate to the message of the banner. Should not be 'heavy' feeling.

```html
<!DOCTYPE html>
<html lang="en">
<head>
<meta charset="utf-8">
<title>BriskTail – Premium Pet Products Delivered</title>
<link href="https://fonts.googleapis.com/css2?family=Arimo:wght@400;700&family=Ubuntu:wght@400;500;700&family=Kalam:wght@400&family=Dancing+Script:wght@600&display=swap" rel="stylesheet">
<style>
  :root {
    --page-bg: #d9e8ec;
    --panel-bg: #f5f7f9;
    --orange: #f47a00;
    --orange-light: #f9a400;
    --green: #8fb51c;
    --green-text: #9bbb1c;
    --blue: #3aa7de;
    --blue-band: #2a8fc1;
    --grey-text: #666a6e;
    --dark-text: #4a4d50;
    --tile-border: #d6dde2;
    --white: #ffffff;
  }
  * { box-sizing: border-box; margin: 0; padding: 0; }
  html, body { width: 1200px; height: 729px; overflow: hidden; }
  body {
    background: var(--page-bg);
    font-family: "Ubuntu", sans-serif;
    position: relative;
  }
  .site-panel {
    position: absolute; left: 85px; top: 7px; width: 1010px; height: 722px;
    background: var(--panel-bg);
  }
  .brand { position: absolute; left: 30px; top: 34px; }
  .brand-name {
    display: flex; align-items: center; gap: 10px;
    font-family: "Ubuntu", sans-serif; font-size: 40px; font-weight: 400;
    color: var(--grey-text); line-height: 1;
  }
  .brand-dot { width: 22px; height: 22px; border-radius: 50%; background: var(--orange); }
  .brand-tagline {
    margin-top: 24px; font-size: 12.5px; letter-spacing: .3px; color: #8a8f94;
  }
  .brand-tagline strong { font-weight: 400; color: var(--dark-text); }
  .account-links {
    position: absolute; right: 30px; top: 31px; display: flex; gap: 14px;
    font-family: "Arimo", sans-serif; font-size: 12px; font-weight: 700; color: var(--dark-text);
  }
  .main-nav {
    position: absolute; left: 29px; top: 143px; width: 950px; height: 52px;
    background: var(--orange); display: flex;
  }
  .nav-home {
    width: 55px; background: var(--green); display: flex; align-items: center; justify-content: center;
  }
  .nav-item {
    font-family: "Arimo", sans-serif; font-size: 18px; color: var(--white);
    display: flex; align-items: center; padding: 0 20px;
    border-left: 1px solid rgba(255,255,255,.55);
  }
  .nav-item:last-of-type { border-right: 1px solid rgba(255,255,255,.55); }
  .search {
    position: absolute; right: 9px; top: 8px; display: flex; height: 34px;
  }
  .search-field { width: 148px; background: var(--white); }
  .search-button {
    width: 97px; background: var(--orange-light); color: var(--white);
    font-family: "Arimo", sans-serif; font-size: 18px;
    display: flex; align-items: center; justify-content: center;
  }
  .hero {
    position: absolute; left: 29px; top: 215px; width: 470px; height: 470px; overflow: hidden;
  }
  .hero-photo {
    position: absolute; inset: 0;
    background: linear-gradient(180deg, #1f3a1a 0%, #3b5a24 45%, #6f5a3a 70%, #4b7f2c 100%);
  }
  .hero-accent {
    position: absolute; left: 96px; top: 21px; width: 374px; height: 10px; background: var(--orange);
  }
  .hero-banner {
    position: absolute; left: 61px; top: 31px; width: 409px; height: 73px;
    background: var(--blue-band); color: var(--white);
    font-family: "Dancing Script", cursive; font-size: 38px; font-weight: 600;
    display: flex; align-items: center; padding-left: 20px;
  }
  .tile {
    position: absolute; width: 229px; height: 229px; background: var(--white);
    border: 1px solid var(--tile-border); overflow: hidden;
  }
  .tile-made { left: 510px; top: 215px; }
  .tile-food { left: 750px; top: 215px; }
  .tile-bulk { left: 510px; top: 455px; }
  .tile-natural { left: 750px; top: 455px; }

  .state-outline {
    position: absolute; left: 18px; top: 6px; width: 200px; height: 214px;
    background: linear-gradient(160deg, #f1f1f1, #e2e2e2);
    border-radius: 18px 30px 40px 60px;
  }
  .made-text { position: absolute; left: 0; right: 0; top: 62px; text-align: center; }
  .made-small { font-size: 22px; color: var(--grey-text); font-weight: 500; }
  .made-large { font-size: 30px; color: var(--blue); font-weight: 500; margin-top: -2px; }

  .food-kicker {
    position: absolute; left: 13px; top: 6px;
    font-family: "Kalam", cursive; font-size: 20px; color: var(--grey-text);
  }
  .food-title {
    position: absolute; left: 14px; top: 40px; color: var(--orange); font-weight: 700; line-height: .95;
  }
  .food-title .big { display: block; font-size: 47px; }
  .food-title .small { display: block; font-size: 28px; }
  .food-bag {
    position: absolute; left: 124px; top: 55px; width: 95px; height: 168px;
    background: linear-gradient(180deg, #b8322a 0%, #8c8a7c 30%, #e0b54a 55%, #c9972c 100%);
    transform: skewY(3deg);
  }

  .badge { position: absolute; left: 14px; top: 10px; }
  .bulk-text { position: absolute; left: 0; right: 0; top: 64px; text-align: center; color: var(--grey-text); }
  .bulk-line { font-size: 17px; line-height: 1.2; }
  .bulk-offer { color: var(--orange-light); font-weight: 500; margin-top: 2px; }
  .bulk-offer .num { font-size: 58px; }
  .bulk-offer .unit { display: inline-block; font-size: 19px; font-weight: 700; text-align: left; line-height: 1; vertical-align: 8px; }

  .natural-head { position: absolute; left: 13px; top: 10px; color: var(--green-text); font-weight: 700; }
  .natural-head .num { font-size: 42px; }
  .natural-head .pct { font-size: 24px; }
  .natural-head .word { font-size: 24px; font-weight: 500; font-family: "Kalam", cursive; }
  .natural-list {
    position: absolute; left: 17px; top: 63px; list-style: none;
    font-size: 13.5px; line-height: 18px; color: var(--dark-text);
  }
  .natural-mascot {
    position: absolute; left: 120px; top: 98px; width: 70px; height: 115px;
    background: radial-gradient(circle at 50% 65%, #a6e02a 0%, #5fae12 60%, #3f8a0c 100%);
    border-radius: 35px 35px 35px 35px / 40px 40px 35px 35px;
  }
</style>
</head>
<body>
  <div class="site-panel">
    <header>
      <div class="brand">
        <div class="brand-name"><span class="brand-dot"></span>BriskTail</div>
        <div class="brand-tagline">PREMIUM PET PRODUCTS <strong>DELIVERED</strong></div>
      </div>
      <nav class="account-links"><span>My Account</span><span>Checkout</span></nav>
    </header>

    <nav class="main-nav">
      <div class="nav-home" aria-label="Home">
        <svg width="16" height="14" viewBox="0 0 16 14"><path d="M8 0 L16 7 L14 7 L14 14 L10 14 L10 9 L6 9 L6 14 L2 14 L2 7 L0 7 Z" fill="#fff"/></svg>
      </div>
      <div class="nav-item">About</div>
      <div class="nav-item">Shop</div>
      <div class="nav-item">Nutrition</div>
      <div class="nav-item">Contact Us</div>
      <div class="search">
        <div class="search-field"></div>
        <div class="search-button">SEARCH</div>
      </div>
    </nav>

    <section class="hero">
      <div class="hero-photo" role="img" aria-label="Photo of a dog and a black cat resting on the grass"></div>
      <div class="hero-accent"></div>
      <div class="hero-banner">Sit. Stay. Let us fetch!</div>
    </section>

    <article class="tile tile-made">
      <div class="state-outline" role="img" aria-label="Outline map of the state of Wisconsin"></div>
      <div class="made-text">
        <div class="made-small">Made in</div>
        <div class="made-large">Wisconsin</div>
      </div>
    </article>

    <article class="tile tile-food">
      <div class="food-kicker">The most awarded</div>
      <div class="food-title"><span class="big">PET</span><span class="small">FOOD</span></div>
      <div class="food-bag" role="img" aria-label="Valmora puppy food bag"></div>
    </article>

    <article class="tile tile-bulk">
      <svg class="badge" width="200" height="210" viewBox="0 0 200 210" aria-hidden="true">
        <circle cx="100" cy="105" r="100" fill="#fbd98a"/>
        <circle cx="100" cy="105" r="90" fill="#fbc94f"/>
        <circle cx="100" cy="105" r="80" fill="#fff"/>
        <circle cx="100" cy="105" r="75" fill="none" stroke="#7a7570" stroke-width="4"/>
      </svg>
      <div class="bulk-text">
        <div class="bulk-line">Bulk Treats</div>
        <div class="bulk-line">Get up to</div>
        <div class="bulk-offer"><span class="num">25</span><span class="unit">%<br>OFF</span></div>
      </div>
    </article>

    <article class="tile tile-natural">
      <div class="natural-head"><span class="num">100</span><span class="pct">%</span> <span class="word">Natural</span></div>
      <ul class="natural-list">
        <li>No Preservatives.</li>
        <li>No Additives.</li>
        <li>Authentic.</li>
        <li>Corvale</li>
        <li>Pup Gnaw.</li>
      </ul>
      <div class="natural-mascot" role="img" aria-label="Illustration of a smiling green apple character"></div>
    </article>
  </div>
</body>
</html>
```